Flyer / marketing email used to solicate work for specialized tree removal equipment.

I'm looking for a flyer for door to door and direct mail distributon. Please utilize as much of the following verbiage as possible...

Breaking news!¿the only 170' grapple crane in use in North American is coming to your neighborhood This revolutionary technology will be in your area for a limited time. Our equipment allows to us accomplish the most challenging tree scenarios with no climber, limited personnel, and amazing efficiency.

This innovation has completely changed the cost of hazardous removals. Call now to get the most competitive estimate yet.

This technology is so limited and in high demand that it can only be in your area for a short time before it has to move on. Get on the list today, it may be months before it makes another round to your neighborhood. ¿

Target Market(s)

Flyers will be delivered in a high end residential neighborhood. Distribution will be on heavy stock and via email.

Colors

Designer to choose colors to be used in the design.

Requirements
Must have
• My logo. Pictures of the crane equipment. Pictures of other tree equipment.
• I'd like a two sided 4" x 5.5" mailer.
• I have permissions to utilize content from the sample one fold flyers I have uploaded.
• I'd like a majority of the content of the Vortalix (aka. Plover limb sample). The light background of the 842 Boughs sample.
• A "BLACK FRIDAY SALE" theme would be awesome.
Nice to have
• Old time breaking news headline married with a high tech innovative feel
• OR
• BLACK FRIDAY SALE theme.

```html
<!DOCTYPE html>
<html lang="en">
<head>
<meta charset="utf-8">
<title>Allday Arbor Co. – Grapple Crane Flyer</title>
<link rel="stylesheet" href="https://fonts.googleapis.com/css2?family=Montserrat:wght@400;700;800&family=Open+Sans:ital,wght@1,800&display=swap">
<style>
:root{
  --green:#22804a;
  --green-dark:#1b6a3c;
  --red:#c8231d;
  --red-dark:#8e1512;
  --orange:#ef4a1c;
  --grey:#dedad8;
  --ring:#eceae8;
  --ink:#2e2e2e;
  --white:#ffffff;
}
*{margin:0;padding:0;box-sizing:border-box}
html,body{width:861px;height:1200px;overflow:hidden;background:#fff}
.flyer{position:relative;width:861px;height:1200px;overflow:hidden;font-family:"Montserrat",sans-serif;background:var(--green)}
.backdrop{position:absolute;inset:0}
.logo-box{position:absolute;left:43px;top:41px;width:245px;height:204px;background:var(--white);display:flex;flex-direction:column;align-items:center;justify-content:center;gap:10px}
.logo-name{font-weight:700;font-size:19px;color:var(--green)}
.logo-phone{font-size:11px;letter-spacing:1px;color:var(--green)}
.logo-mark{width:14px;height:14px;border-radius:50%;background:var(--green)}
.contact-lines{position:absolute;left:440px;top:190px;transform:rotate(-12deg);transform-origin:left top;color:var(--white);font-weight:700;font-size:16px;line-height:21px;letter-spacing:.5px;white-space:nowrap}
.envelope{position:absolute;left:390px;top:204px;transform:rotate(-12deg)}
.headline{position:absolute;left:60px;top:345px;transform:rotate(-14deg);transform-origin:left top;color:var(--white);font-family:"Open Sans",sans-serif;font-style:italic;font-weight:800;font-size:80px;line-height:72px;white-space:nowrap;text-shadow:0 3px 6px rgba(0,0,0,.25)}
.headline .second{display:block;padding-left:30px}
.tagline{position:absolute;left:35px;top:552px;width:400px;transform:rotate(-15deg);transform-origin:center center;color:var(--white);font-weight:700;font-size:16.5px;line-height:22px;letter-spacing:1.6px;text-align:center;text-transform:uppercase;white-space:nowrap}
.body-copy{position:absolute;left:290px;top:602px;width:250px;text-align:right;font-size:17px;line-height:22.7px;color:var(--ink);white-space:nowrap}
.fine-print{position:absolute;left:310px;top:1078px;width:230px;text-align:right;font-size:11.5px;line-height:15.4px;color:var(--white);white-space:nowrap}
.photo{position:absolute;border-radius:50%;border:11px solid var(--ring);width:222px;height:222px}
.photo-crane-truck{left:582px;top:191px;background:radial-gradient(circle at 50% 30%,#c9d6e6,#6f8a5a 70%)}
.photo-flatbed{left:582px;top:442px;background:linear-gradient(#b9b9b7,#5d6a88 60%,#3c3c3c)}
.photo-crane-job{left:590px;top:691px;background:linear-gradient(#c3cddc,#3b4a8f 60%,#3a3a3a)}
.worker-photo{position:absolute;left:24px;top:712px;width:268px;height:488px;background:linear-gradient(#f19a2a 0 12%,#3a4660 30%,#5d6470 70%,#7c7f86);border-radius:110px 110px 0 0}
.site-url{position:absolute;left:822px;top:852px;width:550px;transform:rotate(-90deg);transform-origin:left top;font-weight:800;font-size:19px;line-height:24px;letter-spacing:7px;color:var(--ink);white-space:nowrap;text-align:center}
.cta{position:absolute;left:610px;top:1037px;color:var(--white)}
.cta-label{position:absolute;left:30px;top:0;font-weight:800;font-size:17px;white-space:nowrap}
.cta-phone{position:absolute;left:30px;top:16px;font-weight:800;font-size:24px;white-space:nowrap}
.cta-icon{position:absolute;left:0;top:2px}
.address{position:absolute;left:650px;top:1134px;color:var(--white);font-weight:700;font-size:13.5px;line-height:17px}
.pin-icon{position:absolute;left:608px;top:1137px}
</style>
</head>
<body>
<main class="flyer">
  <svg class="backdrop" width="861" height="1200" viewBox="0 0 861 1200" aria-hidden="true">
    <defs>
      <linearGradient id="redGlow" x1="0" y1="0" x2="1" y2="1">
        <stop offset="0" stop-color="#9c1a15"/>
        <stop offset=".6" stop-color="#d82d1e"/>
        <stop offset="1" stop-color="#f0561f"/>
      </linearGradient>
    </defs>
    <polygon points="640,0 861,0 861,85 685,110" fill="var(--red-dark)"/>
    <polygon points="0,160 375,60 398,245 545,222 552,446 0,600" fill="url(#redGlow)"/>
    <polygon points="0,600 455,490 455,565 0,692" fill="var(--green)"/>
    <polygon points="530,362 861,275 861,955 540,1030 0,1130 0,692 455,565 530,545" fill="var(--grey)"/>
    <polygon points="0,1130 540,1030 555,1060 555,1200 0,1200" fill="var(--red)"/>
    <polygon points="555,1060 861,995 861,1200 555,1200" fill="var(--green)"/>
  </svg>

  <div class="logo-box">
    <span class="logo-mark"></span>
    <span class="logo-name">Allday Arbor Co.</span>
    <span class="logo-phone">- 555.ARBOR.01 -</span>
  </div>

  <svg class="envelope" width="40" height="30" viewBox="0 0 40 30" aria-hidden="true">
    <rect x="2" y="2" width="36" height="26" rx="3" fill="none" stroke="#fff" stroke-width="2.5"/>
    <polyline points="3,4 20,17 37,4" fill="none" stroke="#fff" stroke-width="2.5"/>
  </svg>
  <div class="contact-lines">
    hello@alldayarbor.example<br>
    http://www.alldayarbor.example
  </div>

  <div class="photo photo-crane-truck" role="img" aria-label="Photo of a truck-mounted blue grapple crane at a job site"></div>
  <div class="photo photo-flatbed" role="img" aria-label="Photo of the folded grapple crane on a flatbed truck by a warehouse"></div>
  <div class="photo photo-crane-job" role="img" aria-label="Photo of the grapple crane lifting a tree section over a house"></div>

  <h1 class="headline">BREAKING<span class="second">NEWS</span></h1>

  <p class="tagline">The only 170 grapple crane<br>in use in North American is<br>coming to your neighborhood</p>

  <div class="worker-photo" role="img" aria-label="Photo of a tree service worker in a hard hat and plaid shirt with arms crossed"></div>

  <p class="body-copy">This revolutionary<br>technology will be in<br>your area for a limited<br>time. Our equipment<br>allows to us accomplish<br>the most challenging<br>tree scenarios with no<br>climber, limited<br>personnel, and amazing<br>efficiency.<br>This innovation has<br>completely changed the<br>cost of hazardous<br>removals. Call now to<br>get the most<br>competitive estimate<br>yet.</p>

  <p class="fine-print">This technology is so limited and<br>in high demand that it can only<br>be in your area for a short time<br>before it has to move on. Get on<br>the list today, it may be months<br>before it makes another round to<br>your neighborhood</p>

  <div class="site-url">WWW.ALLDAYARBOR.EXAMPLE</div>

  <div class="cta">
    <svg class="cta-icon" width="20" height="40" viewBox="0 0 20 40" aria-hidden="true">
      <path d="M14 2 C6 4 2 12 2 20 C2 28 6 36 14 38 L18 31 L12 27 C9 23 9 17 12 13 L18 9 Z" fill="#fff"/>
    </svg>
    <span class="cta-label">FOR MORE INFO</span>
    <span class="cta-phone">(555) ARBOR 01</span>
  </div>

  <svg class="pin-icon" width="26" height="34" viewBox="0 0 26 34" aria-hidden="true">
    <path d="M13 2 C6.5 2 2 7 2 13 C2 21 13 32 13 32 C13 32 24 21 24 13 C24 7 19.5 2 13 2 Z" fill="none" stroke="#fff" stroke-width="2"/>
    <circle cx="13" cy="13" r="4.5" fill="none" stroke="#fff" stroke-width="2"/>
  </svg>
  <p class="address">Cedar Hollow,<br>MI 48000</p>
</main>
</body>
</html>
```